Business card design needed

We need a business card for a new business. We are called Little Crew Wearhouse, and we make replica kid size clothing, mainly hi vis shirts, work trousers and shorts. Our long term goal is to include clothing for numerous trades and professions, for our littlest Aussies. We would like a kid friendly card using navy blue, bright orange, bright yellow and bright pink. We haven't set up our web page yet because we want to base it on our final business card design.
Updates

Industry/Entity Type

Clothing

```html
<!DOCTYPE html>
<html lang="en">
<head>
<meta charset="utf-8">
<title>Little Crew Wearhouse – Business Card</title>
<link rel="stylesheet" href="https://fonts.googleapis.com/css2?family=Gochi+Hand&display=swap">
<style>
  :root {
    --purple: #5b4797;
    --pink: #d04697;
    --orange: #d4834a;
    --brand-orange: #f7941d;
    --white: #ffffff;
    --ink: #1a1a1a;
    --card-font: "Gochi Hand", "Comic Sans MS", cursive;
  }
  html, body {
    margin: 0;
    padding: 0;
    width: 1200px;
    height: 741px;
    overflow: hidden;
    background: var(--purple);
  }
  .card {
    position: relative;
    width: 1200px;
    height: 741px;
    overflow: hidden;
    background: var(--purple);
    font-family: var(--card-font);
  }
  .card-shapes {
    position: absolute;
    inset: 0;
  }
  .holder {
    position: absolute;
    top: 30px;
    right: 56px;
    text-align: center;
  }
  .holder-name {
    margin: 0;
    color: var(--white);
    font-size: 62px;
    font-weight: 400;
    line-height: 1;
  }
  .holder-title {
    margin: 4px 0 0;
    color: var(--ink);
    font-size: 33px;
    line-height: 1;
  }
  .brand {
    position: absolute;
    left: 40px;
    top: 250px;
    width: 380px;
    display: flex;
    flex-direction: column;
    align-items: center;
    gap: 18px;
  }
  .brand-dot {
    width: 74px;
    height: 74px;
    border-radius: 50%;
    background: var(--brand-orange);
  }
  .brand-name {
    margin: 0;
    color: var(--white);
    font-size: 54px;
    font-weight: 400;
    line-height: 1.05;
    text-align: center;
  }
  .contact {
    position: absolute;
    left: 530px;
    top: 355px;
    margin: 0;
    padding: 0;
    list-style: none;
    color: var(--white);
    font-size: 48px;
    line-height: 1;
  }
  .contact-item {
    display: flex;
    align-items: center;
    height: 83px;
  }
  .contact-icon {
    width: 26px;
    height: 26px;
    margin-right: 28px;
    flex: none;
  }
  .contact-item.is-continued {
    padding-left: 54px;
  }
</style>
</head>
<body>
  <main class="card">
    <svg class="card-shapes" width="1200" height="741" viewBox="0 0 1200 741" aria-hidden="true">
      <defs>
        <filter id="soft-shadow" x="-10%" y="-10%" width="130%" height="130%">
          <feDropShadow dx="6" dy="4" stdDeviation="6" flood-color="#2a1d55" flood-opacity="0.35"/>
        </filter>
      </defs>
      <polygon class="top-band" points="300,0 1200,0 1200,205 427,103" fill="var(--orange)" filter="url(#soft-shadow)"/>
      <ellipse class="side-panel" cx="162" cy="370" rx="355" ry="556" fill="var(--pink)" filter="url(#soft-shadow)"/>
    </svg>

    <header class="holder">
      <h1 class="holder-name">Your Name</h1>
      <p class="holder-title">Job Title</p>
    </header>

    <div class="brand">
      <span class="brand-dot" role="img" aria-label="Little Crew Wearhouse brand mark"></span>
      <p class="brand-name">Little Crew<br>Wearhouse</p>
    </div>

    <ul class="contact">
      <li class="contact-item">
        <svg class="contact-icon" viewBox="0 0 24 24" aria-hidden="true">
          <path d="M12 1C7.6 1 5 4.2 5 8c0 5 7 15 7 15s7-10 7-15c0-3.8-2.6-7-7-7zm0 10a3 3 0 1 1 0-6 3 3 0 0 1 0 6z" fill="var(--white)"/>
        </svg>
        Your House, Your Street,
      </li>
      <li class="contact-item is-continued">Town, Country-Postcode</li>
      <li class="contact-item">
        <svg class="contact-icon" viewBox="0 0 24 24" aria-hidden="true">
          <rect x="5" y="1" width="14" height="22" rx="2" fill="var(--white)"/>
          <rect x="7.5" y="3.5" width="9" height="7" fill="var(--purple)"/>
          <g fill="var(--purple)">
            <rect x="7.5" y="13" width="2.4" height="2"/><rect x="10.8" y="13" width="2.4" height="2"/><rect x="14.1" y="13" width="2.4" height="2"/>
            <rect x="7.5" y="16.5" width="2.4" height="2"/><rect x="10.8" y="16.5" width="2.4" height="2"/><rect x="14.1" y="16.5" width="2.4" height="2"/>
          </g>
        </svg>
        0123 564789
      </li>
      <li class="contact-item">
        <svg class="contact-icon" viewBox="0 0 24 24" aria-hidden="true">
          <rect x="1.5" y="5" width="21" height="14" fill="none" stroke="var(--white)" stroke-width="1.6"/>
          <path d="M1.5 5l10.5 8 10.5-8M1.5 19l8-7M22.5 19l-8-7" fill="none" stroke="var(--white)" stroke-width="1.6"/>
        </svg>
        you@yourmail.com
      </li>
    </ul>
  </main>
</body>
</html>
```